An innovative software company needs a business card!

We need a business card design for our new innovative software company. Please use the details for the business card provided in business card details section. We will use the business card paper like: https://www.plavex.com/us/products/nfc/business-cards-plus.html Our company name: kelvora We have already a logo and colors to use in business cards too ,

Target Market(s)

App & Sofware Development

Industry/Entity Type

Software

Contact Information for Business Card

Lukas Brenner, BSc.
Owner and Creative Superhero

Adress:
Tulpenweg 37/4/1809
A - 8020, Graz

Tel: +43 (0) 676 921 35 60
Email: lukas.brenner@kelvora.at
Web: www.kelvora.at

Requirements
Must have
• - Use our logo
Nice to have
• It would be nice to have a nice picture on the backside. (About apps, software, technicals or funy stuff) - Use our colors as in business card (optional)

```html
<!DOCTYPE html>
<html lang="en">
<head>
<meta charset="utf-8">
<title>kelvora business card</title>
<link rel="stylesheet" href="https://fonts.googleapis.com/css2?family=Montserrat:wght@400;500;600;700&display=swap">
<style>
:root{
  --cyan:#1bb8d4;
  --cyan-dark:#129fb8;
  --grey-text:#9a9a9a;
  --grey-dark:#7d7d7d;
  --rule:#dcdcdc;
  --card-white:#f7f7f7;
  --stage:#e9e7e3;
  --blue-deep:#1a2f9e;
  --blue-mid:#2a63d8;
  --blue-light:#3fa9e8;
  --band:#e8ecf2;
}
*{margin:0;padding:0;box-sizing:border-box}
html,body{width:1200px;height:780px;overflow:hidden}
body{background:var(--stage);font-family:"Montserrat",sans-serif;position:relative}
.card{position:absolute;top:112px;width:360px;height:556px;border-radius:22px;overflow:hidden;box-shadow:0 10px 28px rgba(0,0,0,.18)}
.card-front{left:170px;background:var(--card-white)}
.card-back{left:670px;background:var(--blue-deep)}

/* front */
.brand-mark{position:absolute;top:92px;left:0;right:0;display:flex;align-items:center;justify-content:center;gap:12px}
.brand-dot{width:34px;height:34px;border-radius:50%;background:var(--cyan)}
.brand-name{font-weight:600;font-size:34px;color:var(--cyan);letter-spacing:.5px}
.identity{position:absolute;top:232px;left:34px;right:34px;text-align:center}
.person-name{font-weight:500;font-size:23px;color:var(--cyan);letter-spacing:.6px}
.person-role{margin-top:4px;font-size:13.5px;color:var(--grey-text);letter-spacing:.8px}
.contact{position:absolute;top:318px;left:34px;right:34px;text-align:center}
.contact-rule{height:1px;background:var(--rule);margin:0 0 12px}
.contact-label{font-size:11px;font-weight:600;color:var(--cyan);letter-spacing:.6px}
.contact-value{font-size:14px;color:var(--grey-dark);letter-spacing:.6px;margin-bottom:10px}
.web-band{position:absolute;left:0;right:0;bottom:0;height:70px;background:var(--cyan);display:flex;align-items:center;justify-content:center;border-top:6px solid #d9d9d9}
.web-address{color:#fff;font-size:17px;letter-spacing:1.2px;font-weight:500}

/* back */
.back-artwork{position:absolute;inset:0;background:radial-gradient(circle at 30% 75%,var(--blue-light) 0%,transparent 45%),radial-gradient(circle at 70% 25%,var(--blue-light) 0%,transparent 40%),linear-gradient(160deg,var(--blue-deep),var(--blue-mid) 55%,var(--blue-deep))}
.back-band{position:absolute;top:0;bottom:0;left:112px;width:136px;background:var(--band);opacity:.94}
.back-brand{position:absolute;top:50%;left:50%;transform:translate(-50%,-50%) rotate(90deg);display:flex;align-items:center;gap:16px;white-space:nowrap}
.back-brand .brand-dot{width:44px;height:44px}
.back-brand .brand-name{font-size:58px;font-weight:700}
.back-tagline{position:absolute;right:8px;top:330px;transform:rotate(90deg);transform-origin:right top;color:#cfe3ff;font-size:22px;letter-spacing:6px;font-weight:500}
</style>
</head>
<body>
<section class="card card-front">
  <div class="brand-mark"><span class="brand-dot"></span><span class="brand-name">kelvora</span></div>
  <div class="identity">
    <p class="person-name">Lukas Brenner, BSc.</p>
    <p class="person-role">Owner and Creative Superhero</p>
  </div>
  <div class="contact">
    <div class="contact-rule"></div>
    <p class="contact-label">Phone</p>
    <p class="contact-value">+43 (0) 676 921 35 60</p>
    <p class="contact-label">Email</p>
    <p class="contact-value">lukas.brenner@kelvora.at</p>
    <p class="contact-label">Address</p>
    <p class="contact-value">Tulpenweg 37/4/1809<br>A - 8020, Graz</p>
  </div>
  <div class="web-band"><span class="web-address">www.kelvora.at</span></div>
</section>

<section class="card card-back">
  <div class="back-artwork" role="img" aria-label="Blue technology illustration with circuit lines, binary code, device icons and a globe"></div>
  <div class="back-band"></div>
  <div class="back-brand"><span class="brand-dot"></span><span class="brand-name">kelvora</span></div>
  <p class="back-tagline">SECURITY</p>
</section>
</body>
</html>
```